Dental Practice - Smiles Ahead - Harbin Arcade - requires New Patient Flyer

We need a flyer to tell prospecting new patients about a new patient offer in our practice, Themed with black and whitewith a bit of colour, and using black and white stripes if possible.
We want to look empathetic, modern and appeal to adults.
The offer is for a complete comprehensive dental examination including all necessary x-rays with no out of pocket expense

Target Market(s)

adults, in particular 30-60 year olds

Industry/Entity Type

Dental

Font styles to use
Sans Serif

Colors
000000
ffffff
cee9f5

Requirements
Must have
• Smiles Ahead
• We are located in the heart of city Adelaide, along the iconic Harbin Arcade.
• Dentist
• Complete comprehensive dental examination including all necessary x-rays
• with $0 out of pocket expense if you have dental health cover.
• No Health fund? We will do it all for you $95.
• With over 50 years combined experience, Dr Victor Pellowski and Dr Stuart Hollen can offer all areas of dental treatment including Preventative, Whitening, Children, General, Cosmetic, Removal, Sedation and Implants.
• (08) 8490 3367
• reception@brightcrestdental.com.au
• Level 2, 74 Harbin Arcade Adelaide SA 5000
• Please try and include all 3 pictures attached
Nice to have
• Cover Plus with KORVA, Accept all health funds, claim on the spot with MEDTAP
Should not have
• colour red, someone not smiling, someone in pain, photo of bad teeth/smile

```html
<!DOCTYPE html>
<html lang="en">
<head>
<meta charset="utf-8">
<title>Smiles Ahead – New Patient Flyer</title>
<link rel="stylesheet" href="https://fonts.googleapis.com/css2?family=Barlow:wght@400;500&display=swap">
<style>
  :root {
    --ink: #1a1a1a;
    --black: #000000;
    --white: #ffffff;
    --sky: #cee9f5;
    --sky-deep: #a9d8ee;
    --grey-text: #5a5a5a;
    --silver-dark: #8c8c8c;
    --badge-blue: #1a9ad9;
    --photo-warm: #ecd3c4;
    --photo-pale: #f7ece6;
    --map-grey: #e6e6e6;
  }
  * { margin: 0; padding: 0; box-sizing: border-box; }
  html, body { width: 848px; height: 1200px; overflow: hidden; background: var(--white); }
  body { font-family: "Barlow", Arial, sans-serif; color: var(--ink); }

  .flyer { position: relative; width: 848px; height: 1200px; overflow: hidden; background: var(--white); }
  .flyer > * { position: absolute; }

  .backdrop { left: 0; top: 0; width: 848px; height: 760px; }

  .hero-photo {
    left: 460px; top: 150px; width: 388px; height: 600px;
    background: linear-gradient(160deg, var(--photo-pale) 0%, var(--photo-warm) 100%);
  }
  .header-sweep { left: 0; top: 0; width: 848px; height: 330px; }

  .brand {
    right: 60px; top: 52px;
    font-size: 42px; font-weight: 500; color: var(--white); letter-spacing: 1px;
  }

  .headline { left: 60px; top: 118px; }
  .headline .lead { font-size: 27px; line-height: 38px; font-weight: 500; }
  .headline .main { font-size: 38px; line-height: 46px; font-weight: 500; }
  .headline .sub { font-size: 26px; line-height: 34px; color: var(--grey-text); letter-spacing: 0.5px; }

  .experience { left: 40px; top: 292px; }
  .experience .over { display: block; margin-left: 137px; font-size: 21px; color: var(--grey-text); }
  .experience .years { display: block; margin: 6px 0 0 36px; font-size: 21px; color: var(--grey-text); }
  .experience .years strong { font-size: 33px; font-weight: 500; color: var(--ink); }
  .experience .doctor { display: block; font-size: 26px; line-height: 40px; }
  .experience .doctor small { font-size: 19px; color: var(--grey-text); }
  .experience .scope { display: block; margin-top: 6px; font-size: 18px; color: var(--grey-text); }

  .services { left: 60px; top: 496px; list-style: none; }
  .services li { font-size: 22px; line-height: 33.3px; padding-left: 19px; position: relative; }
  .services li::before {
    content: ""; position: absolute; left: 0; top: 12px;
    width: 11px; height: 11px; border-radius: 50%; background: var(--silver-dark);
  }

  .promo-band { left: 0; top: 750px; width: 848px; height: 190px; }
  .promo-title {
    left: 196px; top: 758px; font-size: 33px; font-weight: 500; color: var(--white); letter-spacing: 1.3px;
  }
  .exam-strip {
    left: 0; top: 825px; width: 848px; text-align: center;
    font-size: 20px; font-weight: 500; color: var(--white); letter-spacing: 0.4px;
  }
  .offer-covered { left: 30px; top: 868px; font-size: 20px; line-height: 28px; color: var(--grey-text); letter-spacing: 0.3px; }
  .offer-covered strong { font-weight: 500; font-size: 24px; color: var(--ink); letter-spacing: 0.4px; }
  .offer-self { left: 430px; top: 866px; font-size: 20px; line-height: 30px; color: var(--grey-text); letter-spacing: 0.3px; }
  .offer-self strong { font-weight: 500; font-size: 24px; color: var(--ink); }

  .contact-zone {
    left: 0; top: 938px; width: 848px; height: 210px;
    background: linear-gradient(180deg, var(--sky-deep) 0%, var(--sky) 100%);
  }
  .fund-badge { left: 28px; top: 962px; width: 84px; height: 96px; background: var(--badge-blue); border: 3px solid var(--white); }
  .fund-notes { left: 28px; top: 1066px; font-size: 15px; line-height: 24px; font-weight: 500; }

  .location-map {
    left: 272px; top: 952px; width: 297px; height: 188px;
    background: var(--map-grey); border: 1.5px solid var(--ink);
  }
  .location-text { left: 583px; top: 962px; font-size: 17px; line-height: 22px; color: var(--grey-text); letter-spacing: 0.6px; }
  .address { left: 583px; top: 1038px; line-height: 22px; font-style: normal; }
  .address .practice { font-size: 20px; font-weight: 500; display: block; margin-bottom: 2px; letter-spacing: 0.4px; }
  .address span { display: block; font-size: 17px; font-weight: 500; letter-spacing: 0.4px; }

  .footer-tab { left: 0; top: 1146px; width: 848px; height: 54px; }
  .footer { left: 22px; top: 1153px; font-size: 22px; color: var(--ink); letter-spacing: 0.8px; }
  .footer .label { font-weight: 500; }
</style>
</head>
<body>
<main class="flyer">

  <svg class="backdrop" viewBox="0 0 848 760" aria-hidden="true">
    <defs>
      <linearGradient id="skyFade" x1="0" y1="0" x2="0" y2="1">
        <stop offset="0" stop-color="#b4def1"/>
        <stop offset="0.45" stop-color="#ddf0f9"/>
        <stop offset="1" stop-color="#ffffff"/>
      </linearGradient>
    </defs>
    <path d="M0 60 Q380 30 620 170 L620 360 Q300 300 0 340 Z" fill="url(#skyFade)"/>
  </svg>

  <div class="hero-photo" role="img" aria-label="Photo of a smiling woman with bright white teeth"></div>

  <svg class="header-sweep" viewBox="0 0 848 330" aria-hidden="true">
    <defs>
      <linearGradient id="darkSweep" x1="0" y1="0" x2="1" y2="1">
        <stop offset="0" stop-color="#3a3a3a"/>
        <stop offset="0.5" stop-color="#000000"/>
        <stop offset="1" stop-color="#111111"/>
      </linearGradient>
      <linearGradient id="silverLine" x1="0" y1="0" x2="1" y2="0">
        <stop offset="0" stop-color="#ffffff"/>
        <stop offset="0.5" stop-color="#9a9a9a"/>
        <stop offset="1" stop-color="#5c5c5c"/>
      </linearGradient>
    </defs>
    <path d="M0 0 H848 V292 Q760 200 560 130 Q330 55 0 70 Z" fill="url(#darkSweep)"/>
    <path d="M0 70 Q330 55 560 130 Q760 200 848 292 L848 300 Q750 212 550 140 Q320 70 0 86 Z" fill="url(#silverLine)"/>
  </svg>

  <div class="brand">Smiles Ahead</div>

  <header class="headline">
    <div class="lead">Complete Comprehensive</div>
    <div class="main">Dental Examination</div>
    <div class="sub">including all necessary x-rays</div>
  </header>

  <section class="experience">
    <span class="over">With over</span>
    <span class="years"><strong>50 years</strong> combined experience,</span>
    <span class="doctor">Dr Victor Pellowski <small>&amp;</small></span>
    <span class="doctor">Dr Stuart Hollen <small>can offer</small></span>
    <span class="scope">all areas of dental treatment including</span>
  </section>

  <ul class="services">
    <li>Preventative</li>
    <li>Whitening</li>
    <li>Children</li>
    <li>General</li>
    <li>Cosmetic</li>
    <li>Removal</li>
    <li>Sedation and Implants</li>
  </ul>

  <svg class="promo-band" viewBox="0 0 848 190" aria-hidden="true">
    <defs>
      <linearGradient id="greyBar" x1="0" y1="0" x2="0" y2="1">
        <stop offset="0" stop-color="#b8b8b8"/>
        <stop offset="1" stop-color="#6e6e6e"/>
      </linearGradient>
      <linearGradient id="silverPlate" x1="0" y1="0" x2="0" y2="1">
        <stop offset="0" stop-color="#ffffff"/>
        <stop offset="1" stop-color="#c4c4c4"/>
      </linearGradient>
    </defs>
    <polygon points="172,0 848,0 848,62 130,62" fill="url(#greyBar)"/>
    <rect x="0" y="64" width="848" height="44" fill="#000000"/>
    <rect x="0" y="108" width="848" height="80" fill="#000000"/>
    <polygon points="0,108 425,108 365,186 0,186" fill="url(#silverPlate)"/>
    <polygon points="430,108 808,108 748,186 370,186" fill="url(#silverPlate)"/>
  </svg>
  <div class="promo-title">Get “WOW” Whitening Results, Today...</div>
  <div class="exam-strip">Complete Comprehensive Dental Examination including all necessary x-rays</div>
  <div class="offer-covered">With <strong>$0 out of pocket expense</strong><br>if you have dental health cover.</div>
  <div class="offer-self"><strong>No Health fund?</strong><br>We will do it all for you <strong>$95.</strong></div>

  <section class="contact-zone"></section>
  <div class="fund-badge" role="img" aria-label="KORVA Cover Plus partner badge"></div>
  <div class="fund-notes">Accept all health funds<br>Claim on the spot with MEDTAP</div>

  <div class="location-map" role="img" aria-label="Street map showing the practice on Harbin Arcade, Adelaide"></div>

  <p class="location-text">We are located in the<br>heart of city Adelaide,<br>along the iconic Harbin Arcade.</p>
  <address class="address">
    <span class="practice">Smiles Ahead</span>
    <span>Level 2, 74 Harbin Arcade</span>
    <span>Adelaide SA 5000</span>
  </address>

  <svg class="footer-tab" viewBox="0 0 848 54" aria-hidden="true">
    <rect x="0" y="0" width="848" height="54" fill="#ffffff"/>
    <polygon points="740,0 848,0 848,54 790,54" fill="#cee9f5"/>
  </svg>
  <footer class="footer"><span class="label">Contact Us:</span> (08) 8490 3367 &nbsp;|&nbsp; reception@brightcrestdental.com.au</footer>

</main>
</body>
</html>
```